Ferris Contracting LLC Business Card Design

I am looking for a creative and unique business card design. We are a commercial construction general contractor. With the name "FERRIS" Contracting, I am hoping to see some neat designs that correlate with the name.

```html
<!DOCTYPE html>
<html lang="en">
<head>
<meta charset="utf-8">
<title>Ferris Contracting – Business Card</title>
<link rel="stylesheet" href="https://fonts.googleapis.com/css2?family=Michroma&display=swap">
<style>
  :root {
    --stage: #2b2b2b;
    --card: #000000;
    --brand-blue: #2f8fd0;
    --steel: #c9ccd0;
    --text-light: #e6e6e6;
    --deco-grey: #6a6a6a;
    --deco-dark: #1c1c1c;
  }
  * { box-sizing: border-box; margin: 0; padding: 0; }
  html, body {
    width: 1200px; height: 900px; overflow: hidden;
    background: var(--stage);
    font-family: "Michroma", "Arial", sans-serif;
  }
  .stage {
    position: relative; width: 1200px; height: 900px;
  }
  .card {
    position: absolute; top: 295px;
    width: 540px; height: 310px;
    background: var(--card);
    border-radius: 26px;
    overflow: hidden;
  }
  .card--front { left: 40px; }
  .card--back { left: 620px; }

  .blade-decoration {
    position: absolute; top: 0; right: 0;
    width: 240px; height: 310px;
    background: linear-gradient(135deg, var(--deco-grey) 0%, #3d3d3d 55%, var(--deco-dark) 100%);
    opacity: 0.75;
  }
  .card--front .blade-decoration { opacity: 0.45; }

  .wordmark {
    position: absolute;
    display: flex; align-items: center; gap: 14px;
    color: var(--brand-blue);
  }
  .wordmark__dot {
    border-radius: 50%;
    background: var(--brand-blue);
    flex: none;
  }
  .wordmark__text { display: flex; flex-direction: column; line-height: 1; }
  .wordmark__name { letter-spacing: 1px; }
  .wordmark__sub { letter-spacing: 5px; }

  .card--front .wordmark { left: 105px; top: 108px; }
  .card--front .wordmark__dot { width: 22px; height: 22px; }
  .card--front .wordmark__name { font-size: 52px; }
  .card--front .wordmark__sub { font-size: 15px; margin-top: 10px; letter-spacing: 7px; }

  .card--back .wordmark { left: 32px; top: 50px; gap: 8px; }
  .card--back .wordmark__dot { width: 12px; height: 12px; }
  .card--back .wordmark__name { font-size: 26px; }
  .card--back .wordmark__sub { font-size: 7.5px; margin-top: 5px; letter-spacing: 3.6px; }

  .person {
    position: absolute; right: 30px; top: 186px; text-align: right;
  }
  .person__name { color: var(--brand-blue); font-size: 15px; }
  .person__role { color: var(--text-light); font-size: 10px; margin-top: 4px; }

  .address {
    position: absolute; left: 32px; bottom: 26px;
    color: var(--text-light); font-size: 10.5px; line-height: 16px;
    font-style: normal;
  }
  .contacts {
    position: absolute; right: 30px; bottom: 26px;
    list-style: none; text-align: right;
    color: var(--text-light); font-size: 10.5px; line-height: 16px;
  }
  .contacts li { display: flex; justify-content: flex-end; align-items: center; gap: 8px; }
  .contacts svg { width: 11px; height: 11px; fill: var(--brand-blue); flex: none; }
</style>
</head>
<body>
<main class="stage">

  <section class="card card--front" aria-label="Card front">
    <div class="blade-decoration" role="img" aria-label="Large saw-blade brand decoration"></div>
    <div class="wordmark">
      <span class="wordmark__dot"></span>
      <span class="wordmark__text">
        <span class="wordmark__name">FERRIS</span>
        <span class="wordmark__sub">CONTRACTING</span>
      </span>
    </div>
  </section>

  <section class="card card--back" aria-label="Card back">
    <div class="blade-decoration" role="img" aria-label="Large saw-blade brand decoration"></div>
    <div class="wordmark">
      <span class="wordmark__dot"></span>
      <span class="wordmark__text">
        <span class="wordmark__name">FERRIS</span>
        <span class="wordmark__sub">CONTRACTING</span>
      </span>
    </div>

    <div class="person">
      <p class="person__name">MARCUS DELANEY</p>
      <p class="person__role">MANAGING DIRECTOR</p>
    </div>

    <address class="address">
      48 Ironwood Avenue<br>
      Millbrook, New York<br>
      12545
    </address>

    <ul class="contacts">
      <li>555 0142 7788
        <svg viewBox="0 0 24 24"><path d="M6.6 10.8a15.1 15.1 0 0 0 6.6 6.6l2.2-2.2c.3-.3.7-.4 1-.2 1.1.4 2.3.6 3.6.6.6 0 1 .4 1 1V20c0 .6-.4 1-1 1A17 17 0 0 1 3 4c0-.6.4-1 1-1h3.5c.6 0 1 .4 1 1 0 1.3.2 2.5.6 3.6.1.3 0 .7-.2 1z"/></svg>
      </li>
      <li>info@ferriscontracting.com
        <svg viewBox="0 0 24 24"><path d="M2 5h20v14H2z M3 6l9 7 9-7" fill="none" stroke="#2f8fd0" stroke-width="2"/><path d="M2 5h20v2l-10 7L2 7z"/></svg>
      </li>
      <li>www.ferriscontracting.com
        <svg viewBox="0 0 24 24"><circle cx="12" cy="12" r="9" fill="none" stroke="#2f8fd0" stroke-width="2"/><path d="M3 12h18M12 3c3 3 3 15 0 18M12 3c-3 3-3 15 0 18" fill="none" stroke="#2f8fd0" stroke-width="1.6"/></svg>
      </li>
    </ul>
  </section>

</main>
</body>
</html>
```